WordPress Website Design Project

Technical & Functional Deliverables
WordPress CMS
Fully responsive design
Integrated WhatsApp chatbot
Custom article filtering system
SEO-friendly site structure & performance optimization
CMS user manual & training session
Updates

Need extra days to review

Industry/Entity Type

Industrial Safety and Compliance

Coding

Coded - Design and coding required

Number of Pages Required

5+ page

Font styles to use
Sans Serif

Colors
0054AA
0677BA
7BADD7
CADEEF
E8F1F8

```html
<!DOCTYPE html>
<html lang="en">
<head>
<meta charset="utf-8">
<title>Bastion — Industrial Safety &amp; Compliance</title>
<link href="https://fonts.googleapis.com/css2?family=Archivo:wght@400;500;600;700;800&display=swap" rel="stylesheet">
<style>
:root{
  --navy:#1d2a4a;
  --blue:#0054aa;
  --blue-mid:#0677ba;
  --blue-soft:#7badd7;
  --blue-pale:#cadeef;
  --blue-mist:#e8f1f8;
  --accent:#5b8fd0;
  --ink:#1b2437;
  --text:#333a45;
  --grey-bg:#f5f5f5;
  --white:#ffffff;
  --black:#0b0b0b;
}
*{margin:0;padding:0;box-sizing:border-box}
html,body{width:1200px;height:4640px;overflow:hidden}
body{font-family:"Archivo",sans-serif;color:var(--text);background:var(--white);position:relative}
.abs{position:absolute}
section{position:absolute;left:0;width:1200px}

/* hero */
.hero{top:0;height:649px;background:linear-gradient(120deg,#0d1c3f 0%,#16336a 40%,#1f4c8c 65%,#0d1a36 100%)}
.hero-photo{position:absolute;inset:0;background:radial-gradient(ellipse at 70% 40%,rgba(120,170,230,.45),transparent 55%),radial-gradient(ellipse at 20% 85%,rgba(60,130,220,.5),transparent 50%),linear-gradient(180deg,rgba(10,20,45,.2),rgba(10,20,45,.55))}
.brand{display:flex;align-items:center;gap:6px;color:var(--white);font-weight:800;font-size:30px;letter-spacing:1px}
.brand .mark{width:34px;height:34px;background:var(--white)}
.hero .brand{left:126px;top:38px}
.nav{top:46px;left:0;width:1200px;height:20px}
.nav a{position:absolute;color:var(--white);font-size:12.5px;font-weight:600;text-decoration:none;letter-spacing:.2px}
.hero h1{left:126px;top:218px;color:var(--white);font-size:45px;line-height:53px;font-weight:800;letter-spacing:-.5px;width:520px}
.cta{left:126px;top:403px;width:178px;height:44px;border:1.5px solid var(--white);display:flex;align-items:center}
.cta .mark{width:40px;height:40px;background:var(--white);margin-left:2px}
.cta span{color:var(--white);font-size:14px;font-weight:700;margin-left:14px}

/* values */
.values{top:649px;height:882px;background:var(--white)}
.sec-title{color:var(--ink);font-weight:800;font-size:42px;letter-spacing:-.3px}
.values .sec-title{top:95px;width:1200px;text-align:center}
.values .lead{top:156px;width:1200px;text-align:center;color:var(--ink);font-size:29px;font-weight:500;line-height:36px}
.frame{left:126px;top:318px;width:258px;height:397px;border:5px solid var(--accent)}
.worker-photo{left:187px;top:275px;width:362px;height:400px;background:linear-gradient(135deg,#b8a988 0%,#5b6a7c 45%,#2a3a4f 100%)}
.blue-tile{left:65px;top:540px;width:211px;height:227px;background:var(--accent)}
.values-copy{left:612px;top:271px;width:460px}
.values-copy h3{color:var(--ink);font-size:21px;font-weight:600;margin-bottom:14px}
.values-copy p{font-size:14px;line-height:16px;margin-bottom:17px;color:var(--text)}
.values-copy b{font-weight:600;color:var(--ink)}

/* work */
.work{top:1531px;height:880px;background:var(--grey-bg)}
.work .sec-title{left:126px;top:103px}
.work .intro{left:404px;top:113px;width:580px;font-size:13.5px;line-height:17px}
.arrows{top:112px;left:1034px;display:flex;gap:14px}
.card-lg{left:126px;top:224px;width:447px;height:383px;background:linear-gradient(180deg,#d9dee4 0%,#a9b4bf 45%,#5e6a6e 100%)}
.work .cap-lg{left:126px;top:634px;width:440px;color:var(--ink);font-size:29px;line-height:34px;font-weight:600}
.work .txt-lg{left:128px;top:714px;width:430px;font-size:13.5px;line-height:17px}
.card-sm{top:224px;height:291px}
.card-sm.a{left:605px;width:287px;background:linear-gradient(180deg,#3a5f93 0%,#6b6a5a 55%,#c28a3d 100%)}
.card-sm.b{left:924px;width:276px;background:linear-gradient(160deg,#8db3db 0%,#d6b03a 55%,#3d6fae 100%)}
.cap-sm{top:533px;color:var(--ink);font-size:21px;line-height:25px;font-weight:600;width:270px}

/* clients */
.clients{top:2411px;height:580px}
.clients .band{position:absolute;left:0;top:0;width:1200px;height:475px;background:var(--navy)}
.clients .panel{left:77px;top:119px;width:1045px;height:461px;background:var(--white);box-shadow:0 20px 40px rgba(0,0,0,.08)}
.clients .sec-title{top:190px;width:1200px;text-align:center}
.clients .intro{top:235px;width:1200px;text-align:center;font-size:13.5px;line-height:20px}
.logo-grid{left:126px;top:304px;width:946px;display:grid;grid-template-columns:repeat(5,178px);column-gap:14px;row-gap:16px}
.logo-cell{height:95px;border:1.5px solid #d7dbe3;display:flex;align-items:center;justify-content:center;gap:8px;font-size:20px;font-weight:700;color:var(--navy)}
.logo-cell i{display:block;width:14px;height:14px;background:var(--navy)}

/* solutions */
.solutions{top:2991px;height:706px}
.solutions .sec-title{top:122px;width:1200px;text-align:center}
.sol-card{top:194px;width:225px;height:361px;border:1px solid #c9ced8;border-bottom:4px solid var(--accent);background:var(--white)}
.sol-img{height:278px}
.sol-label{position:absolute;left:13px;top:295px;font-size:14px;line-height:16px;color:var(--ink)}
.sol-arrow{position:absolute;right:12px;top:302px}

/* people */
.people{top:3697px;height:577px;background:var(--grey-bg)}
.people .sec-title{top:103px;width:1200px;text-align:center}
.person{top:166px;width:240px;text-align:center}
.avatar{width:223px;height:223px;border-radius:50%;margin:0 auto;background:radial-gradient(circle at 50% 40%,#9fc2e8,#5b8fd0 70%)}
.person h4{margin-top:25px;font-size:23px;font-weight:600;color:var(--ink)}
.person p{margin-top:6px;font-size:16px;color:#5a6270}

/* footer */
.footer{top:4274px;height:366px;background:var(--black);color:var(--white)}
.footer .tag{left:126px;top:89px;font-size:20px;line-height:30px;font-weight:700;width:300px}
.fcol{top:84px;font-size:11.5px;font-weight:600;line-height:24px}
.fcol a{display:block;color:var(--white);text-decoration:none}
.footer .rule{left:126px;top:223px;width:946px;height:1px;background:#4a4a4a}
.legal{left:127px;top:254px;font-size:10.5px;font-weight:600}
.follow{left:127px;top:297px;font-size:10.5px;font-weight:600;display:flex;align-items:center;gap:10px}
.follow i{display:block;width:26px;height:26px;background:var(--blue-mid)}
.footer .brand{left:946px;top:255px;font-size:27px}
.footer .brand .mark{width:28px;height:28px}
.copy{left:830px;top:300px;width:256px;text-align:right;font-size:12.5px}
</style>
</head>
<body>

<section class="hero">
  <div class="hero-photo" role="img" aria-label="Night view of an illuminated oil refinery with towers and pipework"></div>
  <div class="abs brand"><span class="mark"></span>BASTION</div>
  <nav class="abs nav">
    <a href="#" style="left:671px">HOME</a>
    <a href="#" style="left:759px">ABOUT US</a>
    <a href="#" style="left:880px">SOLUTIONS</a>
    <a href="#" style="left:1009px">ARTICLES</a>
  </nav>
  <h1 class="abs">YOUR PARTNER IN INDUSTRIAL SAFETY &amp; COMPLIANCE</h1>
  <a class="abs cta" href="#"><span class="mark"></span><span>CONTACT US</span></a>
</section>

<section class="values">
  <h2 class="abs sec-title">OUR VALUES</h2>
  <p class="abs lead">We are Bastion: Your Partner in<br>Industrial Safety and Compliance.</p>
  <div class="abs frame"></div>
  <div class="abs worker-photo" role="img" aria-label="Engineer in a hard hat adjusting a valve on industrial equipment"></div>
  <div class="abs blue-tile"></div>
  <div class="abs values-copy">
    <h3>Mission Statement and Core Values</h3>
    <p>To provide expert guidance and practical solutions in industrial safety and compliance, delivering clarity, reliability, and peace of mind to every partner we serve.</p>
    <p>We achieve this mission by staying true to our foundational values:</p>
    <p><b>Assurance:</b> Providing confidence through technically robust solutions.</p>
    <p><b>Reliability:</b> Ensuring consistent performance in demanding situations.</p>
    <p><b>Commitment:</b> Fulfilling promises and exceeding expectations.</p>
    <p><b>Honor:</b> Upholding the highest ethical standards.</p>
    <p><b>Expertise:</b> Leveraging deep industry knowledge to solve complex challenges.</p>
    <p><b>Responsibility:</b> Taking full accountability from concept through completion.</p>
  </div>
</section>

<section class="work">
  <h2 class="abs sec-title">OUR WORK</h2>
  <p class="abs intro">Lorem ipsum dolor sit amet, consectetur adipiscing elit, sed do eiusmod tempor incididunt ut labore et dolore magna aliqua. Quis ipsum suspendisse.</p>
  <div class="abs arrows">
    <svg width="46" height="20" viewBox="0 0 46 20"><path d="M44 10H3M11 2L3 10l8 8" fill="none" stroke="#1b2437" stroke-width="2.5"/></svg>
    <svg width="46" height="20" viewBox="0 0 46 20"><path d="M2 10h41M35 2l8 8-8 8" fill="none" stroke="#1b2437" stroke-width="2.5"/></svg>
  </div>
  <div class="abs card-lg" role="img" aria-label="Safety inspector in high-visibility vest standing on an industrial platform"></div>
  <h3 class="abs cap-lg">Lorem ipsum dolor sit amet, consectetur adipiscin.</h3>
  <p class="abs txt-lg">Lorem ipsum dolor sit amet, consectetur adipiscing elit, sed do eiusmod tempor incididunt ut labore et dolore magna aliqua. Quis ipsum suspendisse.</p>
  <div class="abs card-sm a" role="img" aria-label="Storage tanks at a refinery lit at dusk"></div>
  <h3 class="abs cap-sm" style="left:603px">Lorem ipsum dolor sit amet consectetur</h3>
  <div class="abs card-sm b" role="img" aria-label="Yellow gas pipelines and valves at a processing station"></div>
  <h3 class="abs cap-sm" style="left:929px">Lorem ipsum dolor sit amet consectetur</h3>
</section>

<section class="clients">
  <div class="band"></div>
  <div class="abs panel"></div>
  <h2 class="abs sec-title">OUR CLIENTS</h2>
  <p class="abs intro">Lorem ipsum dolor sit amet, consectetur adipiscing elit, sed do eiusmod tempor<br>incididunt ut labore et dolore magna aliqua. Quis ipsum suspendisse.</p>
  <div class="abs logo-grid">
    <div class="logo-cell"><i></i>Veltra</div>
    <div class="logo-cell">Orrin Studio</div>
    <div class="logo-cell">K+M</div>
    <div class="logo-cell">Dune</div>
    <div class="logo-cell">RQS</div>
    <div class="logo-cell" style="font-size:15px"><i></i>Framecore Consulting</div>
    <div class="logo-cell" style="font-size:17px">Halden Group</div>
    <div class="logo-cell">NVA</div>
    <div class="logo-cell"><i></i>Tresco</div>
    <div class="logo-cell" style="font-size:18px">Marlow Keane</div>
  </div>
</section>

<section class="solutions">
  <h2 class="abs sec-title">OUR SOLUTIONS</h2>
  <div class="abs sol-card" style="left:122px">
    <div class="sol-img" role="img" aria-label="Hand touching a digital engineering interface" style="background:linear-gradient(160deg,#2b5f9a,#7badd7 60%,#cadeef)"></div>
    <p class="sol-label">Engineering<br>&amp; design</p>
    <svg class="sol-arrow" width="22" height="12" viewBox="0 0 22 12"><path d="M1 6h19M15 1l5 5-5 5" fill="none" stroke="#1b2437" stroke-width="1.6"/></svg>
  </div>
  <div class="abs sol-card" style="left:366px">
    <div class="sol-img" role="img" aria-label="Laptop with technical support icons" style="background:linear-gradient(160deg,#6d86a8,#1f3352 60%,#0e1a2e)"></div>
    <p class="sol-label">Technical Support &amp;<br>Site Services</p>
    <svg class="sol-arrow" width="22" height="12" viewBox="0 0 22 12"><path d="M1 6h19M15 1l5 5-5 5" fill="none" stroke="#1b2437" stroke-width="1.6"/></svg>
  </div>
  <div class="abs sol-card" style="left:609px">
    <div class="sol-img" role="img" aria-label="Interlocking gears representing risk management" style="background:linear-gradient(160deg,#1a3558,#3d6fa3 55%,#142640)"></div>
    <p class="sol-label">Risk Management &amp;<br>Compliance Services</p>
    <svg class="sol-arrow" width="22" height="12" viewBox="0 0 22 12"><path d="M1 6h19M15 1l5 5-5 5" fill="none" stroke="#1b2437" stroke-width="1.6"/></svg>
  </div>
  <div class="abs sol-card" style="left:850px">
    <div class="sol-img" role="img" aria-label="Water spilling from dam gates in white spray" style="background:linear-gradient(180deg,#a9c6e4,#e8eef4 55%,#cfd6de)"></div>
    <p class="sol-label">Transitioning to<br>Fluorine-Free Foam</p>
    <svg class="sol-arrow" width="22" height="12" viewBox="0 0 22 12"><path d="M1 6h19M15 1l5 5-5 5" fill="none" stroke="#1b2437" stroke-width="1.6"/></svg>
  </div>
</section>

<section class="people">
  <h2 class="abs sec-title">OUR PEOPLE</h2>
  <svg class="abs" style="left:36px;top:282px" width="46" height="20" viewBox="0 0 46 20"><path d="M44 10H3M11 2L3 10l8 8" fill="none" stroke="#1b2437" stroke-width="2.5"/></svg>
  <svg class="abs" style="left:1118px;top:282px" width="46" height="20" viewBox="0 0 46 20"><path d="M2 10h41M35 2l8 8-8 8" fill="none" stroke="#1b2437" stroke-width="2.5"/></svg>
  <div class="abs person" style="left:118px"><div class="avatar" role="img" aria-label="Portrait of a project manager in a yellow hard hat and safety vest"></div><h4>Alres Bore</h4><p>Project Manager</p></div>
  <div class="abs person" style="left:357px"><div class="avatar" role="img" aria-label="Portrait of a project manager in a yellow hard hat and safety vest"></div><h4>Alres Bore</h4><p>Project Manager</p></div>
  <div class="abs person" style="left:599px"><div class="avatar" role="img" aria-label="Portrait of a project manager in a white hard hat and safety glasses"></div><h4>Alres Bore</h4><p>Project Manager</p></div>
  <div class="abs person" style="left:838px"><div class="avatar" role="img" aria-label="Portrait of a project manager in an orange hard hat"></div><h4>Alres Bore</h4><p>Project Manager</p></div>
</section>

<footer class="abs footer" style="left:0;width:1200px">
  <p class="abs tag">WE ARE BASTION. YOUR PARTNER IN INDUSTRIAL SAFETY AND COMPLIANCE</p>
  <div class="abs fcol" style="left:798px"><a href="#">HOME</a><a href="#">ABOUT US</a><a href="#">SOLUTIONS</a><a href="#">ARTICLES</a></div>
  <div class="abs fcol" style="left:958px"><a href="#">OUR WORK</a><a href="#">CONTACT US</a><a href="#">WHITE PAPERS</a><a href="#">NEWS</a></div>
  <div class="abs rule"></div>
  <p class="abs legal">LEGAL &nbsp;|&nbsp; COOKIES &nbsp;|&nbsp; PRIVACY</p>
  <div class="abs follow">FOLLOW US <i></i></div>
  <div class="abs brand"><span class="mark"></span>BASTION</div>
  <p class="abs copy">©BASTION 2025. All Righst Are Reserved.</p>
</footer>

</body>
</html>
```